Business card for massage therapy company called Blue Fern Wellness

Need business card for massage therapy company called Blue Fern Wellness. Would like my logo on the front and the back of the card I have 3 options of logos and you can play with what looks better.

Would like this information displayed on the back of the card:

Marcus Ellery
Licensed Massage Therapist
415-903-2264
bluefern-wellness.example
bluefern_wellness_

```html
<!DOCTYPE html>
<html lang="en">
<head>
<meta charset="utf-8">
<title>Blue Fern Wellness – Business Card</title>
<link rel="stylesheet" href="https://fonts.googleapis.com/css2?family=Raleway:wght@300;400&family=Open+Sans:wght@400&display=swap">
<style>
  :root {
    --backdrop: #2b2b2c;
    --card-light: #ebebea;
    --sage: #595e44;
    --sage-light: #6c7255;
    --sage-text: #4f5540;
    --clay: #c28d69;
    --ink: #3d3f37;
  }
  * { margin: 0; padding: 0; box-sizing: border-box; }
  html, body {
    width: 1200px; height: 801px; overflow: hidden;
    background: var(--backdrop);
  }
  .stage {
    position: relative; width: 1200px; height: 801px;
    display: flex; align-items: center; justify-content: center; gap: 60px;
  }
  .card {
    position: relative; width: 520px; height: 297px;
    border-radius: 22px; overflow: hidden;
    box-shadow: 0 14px 30px rgba(0,0,0,.35);
  }
  .card--front { background: var(--card-light); }
  .card--back { background: var(--sage); }

  .front-identity {
    position: absolute; left: 40px; top: 66px;
  }
  .front-name {
    font-family: "Raleway", sans-serif; font-weight: 300;
    font-size: 33px; letter-spacing: 1.5px; line-height: 1.1;
    color: var(--sage-text); white-space: nowrap;
  }
  .front-title {
    margin-top: 8px;
    font-family: "Open Sans", sans-serif; font-size: 12.5px;
    letter-spacing: .6px; color: var(--clay);
  }
  .front-brand {
    position: absolute; right: 32px; top: 66px;
    display: flex; align-items: center; gap: 10px;
  }
  .front-brand__circle {
    flex: none; width: 42px; height: 42px; border-radius: 50%;
    border: 1.5px solid var(--sage-text);
  }
  .front-brand__name {
    font-family: "Raleway", sans-serif; font-weight: 400;
    font-size: 13px; letter-spacing: 2px; line-height: 1.4;
    text-transform: uppercase; color: var(--sage-text); width: 96px;
  }
  .front-rule {
    position: absolute; left: 32px; right: 32px; top: 168px;
    height: 1px; background: var(--sage-text);
  }
  .contacts {
    position: absolute; left: 32px; right: 32px; top: 194px;
    display: flex; justify-content: space-between; align-items: center;
    list-style: none;
  }
  .contact {
    display: flex; align-items: center; gap: 7px; white-space: nowrap;
    font-family: "Open Sans", sans-serif; font-size: 12.5px;
    letter-spacing: .2px; color: var(--ink);
  }
  .contact svg { width: 12px; height: 12px; flex: none; }
  .front-edge {
    position: absolute; left: 0; right: 0; bottom: 0; height: 32px;
    background: var(--sage);
    border-top: 5px solid var(--clay);
  }
  .front-edge::before {
    content: ""; position: absolute; left: 0; right: 0; top: -9px;
    height: 4px; background: var(--card-light);
  }

  .back-mark {
    position: absolute; left: 50%; top: 50%;
    transform: translate(-50%, -50%);
    display: flex; flex-direction: column; align-items: center; gap: 14px;
  }
  .back-mark__circle {
    width: 120px; height: 120px; border-radius: 50%;
    border: 2px solid var(--sage-light);
  }
  .back-mark__name {
    font-family: "Raleway", sans-serif; font-weight: 400;
    font-size: 15px; letter-spacing: 3px; text-transform: uppercase;
    color: var(--sage-light); white-space: nowrap;
  }
</style>
</head>
<body>
<main class="stage">
  <section class="card card--front" aria-label="Card front">
    <div class="front-identity">
      <h1 class="front-name">Marcus Ellery</h1>
      <p class="front-title">Licensed Massage Therapist</p>
    </div>
    <div class="front-brand">
      <span class="front-brand__circle"></span>
      <span class="front-brand__name">Blue Fern Wellness</span>
    </div>
    <div class="front-rule"></div>
    <ul class="contacts">
      <li class="contact">
        <svg viewBox="0 0 14 14" fill="none" stroke="#c28d69" stroke-width="1.2"><path d="M3 1.5h2l1 3-1.5 1a7 7 0 0 0 4 4l1-1.5 3 1v2a1.5 1.5 0 0 1-1.5 1.5A11 11 0 0 1 1.5 3 1.5 1.5 0 0 1 3 1.5z"/></svg>
        415-903-2264
      </li>
      <li class="contact">
        <svg viewBox="0 0 14 14" fill="none" stroke="#c28d69" stroke-width="1.2"><rect x="1" y="3" width="12" height="8"/><path d="M1 3l6 5 6-5"/></svg>
        bluefern_wellness_
      </li>
      <li class="contact">
        <svg viewBox="0 0 14 14" fill="none" stroke="#c28d69" stroke-width="1.1"><circle cx="7" cy="7" r="6"/><ellipse cx="7" cy="7" rx="2.6" ry="6"/><path d="M1 7h12M2 4h10M2 10h10"/></svg>
        bluefern-wellness.example
      </li>
    </ul>
    <div class="front-edge"></div>
  </section>

  <section class="card card--back" aria-label="Card back">
    <div class="back-mark">
      <span class="back-mark__circle"></span>
      <span class="back-mark__name">Blue Fern Wellness</span>
    </div>
  </section>
</main>
</body>
</html>
```